Delegate Welcome sign

The Copperfield Lodge hotel in Pine Bush NY is welcoming delegations from many different countries during 2019. We want to make a welcome sign about 16:9 ratio about 4 feet high with raised letters. I have attached a background design that we liked and a template with the wording. As you will see I need help with it.

```html
<!DOCTYPE html>
<html lang="en">
<head>
<meta charset="utf-8">
<title>Copperfield Lodge – Delegate Welcome Sign</title>
<link href="https://fonts.googleapis.com/css2?family=Great+Vibes&family=Tinos:wght@400;700&display=swap" rel="stylesheet">
<style>
  :root {
    --bg-centre: #3f4c48;
    --bg-mid: #343f3c;
    --bg-edge: #283130;
    --gold: #f4b81e;
    --gold-light: #f7c52c;
    --orange: #f0902a;
    --orange-deep: #ec8a1f;
    --leaf: #6e9b90;
    --leaf-deep: #3f6a60;
    --ink-light: #eeeeea;
  }
  * { margin: 0; padding: 0; box-sizing: border-box; }
  html, body { width: 1200px; height: 677px; overflow: hidden; background: var(--bg-edge); }
  .sign {
    position: relative;
    width: 1200px;
    height: 677px;
    overflow: hidden;
    background: radial-gradient(ellipse 60% 65% at 50% 42%, var(--bg-centre) 0%, var(--bg-mid) 55%, var(--bg-edge) 100%);
    text-align: center;
  }
  .foliage {
    position: absolute;
    top: 0;
    width: 390px;
    height: 225px;
  }
  .foliage--left { left: 0; }
  .foliage--right { right: 0; }

  .brand {
    position: absolute;
    top: 112px;
    left: 0;
    width: 100%;
    font-family: "Tinos", serif;
    font-weight: 400;
    font-size: 30px;
    letter-spacing: 3px;
    line-height: 1;
    color: var(--gold);
  }

  .welcome {
    position: absolute;
    top: 170px;
    left: 0;
    width: 100%;
    font-family: "Great Vibes", cursive;
    font-weight: 400;
    font-size: 112px;
    line-height: 1.1;
    color: var(--gold);
  }

  .divider {
    position: absolute;
    top: 318px;
    left: 182px;
    width: 836px;
    height: 68px;
  }

  .headline {
    position: absolute;
    top: 400px;
    left: 0;
    width: 100%;
    font-family: "Tinos", serif;
    font-weight: 700;
    font-size: 60px;
    line-height: 1;
    letter-spacing: 0.5px;
    background: linear-gradient(90deg, var(--orange-deep) 0%, var(--gold-light) 45%, var(--gold) 60%, var(--orange-deep) 100%);
    -webkit-background-clip: text;
    background-clip: text;
    color: transparent;
  }

  .location {
    position: absolute;
    top: 498px;
    left: 0;
    width: 100%;
    font-family: "Tinos", serif;
    font-weight: 700;
    font-size: 30px;
    line-height: 36px;
    color: var(--gold);
  }

  .hashtag {
    position: absolute;
    top: 630px;
    left: 0;
    width: 100%;
    font-family: "Tinos", serif;
    font-weight: 400;
    font-size: 24px;
    letter-spacing: 2px;
    line-height: 1;
    color: var(--ink-light);
  }
</style>
</head>
<body>
<main class="sign">
  <svg class="foliage foliage--left" viewBox="0 0 390 225" role="img" aria-label="Decorative sprays of sage-green leaves and golden berries in the top left corner">
    <defs>
      <radialGradient id="foliageLeft" cx="35%" cy="20%" r="75%">
        <stop offset="0%" stop-color="#6e9b90" stop-opacity="0.8"/>
        <stop offset="55%" stop-color="#3f6a60" stop-opacity="0.5"/>
        <stop offset="100%" stop-color="#3f6a60" stop-opacity="0"/>
      </radialGradient>
    </defs>
    <ellipse cx="170" cy="40" rx="230" ry="170" fill="url(#foliageLeft)"/>
  </svg>

  <svg class="foliage foliage--right" viewBox="0 0 390 225" role="img" aria-label="Decorative sprays of sage-green leaves and golden berries in the top right corner">
    <defs>
      <radialGradient id="foliageRight" cx="65%" cy="20%" r="75%">
        <stop offset="0%" stop-color="#6e9b90" stop-opacity="0.8"/>
        <stop offset="55%" stop-color="#3f6a60" stop-opacity="0.5"/>
        <stop offset="100%" stop-color="#3f6a60" stop-opacity="0"/>
      </radialGradient>
    </defs>
    <ellipse cx="220" cy="40" rx="230" ry="170" fill="url(#foliageRight)"/>
  </svg>

  <header class="brand">COPPERFIELD LODGE</header>

  <h1 class="welcome">Welcomes</h1>

  <svg class="divider" viewBox="0 0 836 68">
    <defs>
      <linearGradient id="ruleGold" x1="0" x2="1">
        <stop offset="0%" stop-color="#f0902a"/>
        <stop offset="100%" stop-color="#f4b81e"/>
      </linearGradient>
      <radialGradient id="flourishTone" cx="50%" cy="50%" r="50%">
        <stop offset="0%" stop-color="#f4b81e" stop-opacity="0.55"/>
        <stop offset="100%" stop-color="#f4b81e" stop-opacity="0"/>
      </radialGradient>
    </defs>
    <rect x="0" y="19" width="118" height="6" fill="url(#ruleGold)"/>
    <rect x="718" y="19" width="118" height="6" fill="url(#ruleGold)"/>
    <rect x="134" y="4" width="568" height="60" rx="30" fill="url(#flourishTone)" role="img" aria-label="Golden scroll flourish ornament"/>
  </svg>

  <h2 class="headline">2019 INTERNATIONAL DELEGATES</h2>

  <p class="location">TO THE HUDSON VALLEY<br>IN NEW YORK</p>

  <p class="hashtag">#COPPERFIELDLODGEHOTEL</p>
</main>
</body>
</html>
```